Identification Supplier website

Front and product page designs required for this Business Catalyst website for an identification supply company.

Also interested in coding same into finished site for additional fee.

Client is a security/event ID supplies company selling identification products like card holders, printers, lanyards, clips and so on.

Current placeholder site is at:
http://www.tagmorrow.com.au/

Other sites the client likes are at:

www.varrowdesigns.com.au

www.badgenook.com.au

www.qrv.com.au

http://start42.brimfield.co.nz/online/welcome.csn

Otherwise colour scheme should follow logo and structure should follow wireframe attached.

Industry/Entity Type

Business

```html
<!DOCTYPE html>
<html lang="en">
<head>
<meta charset="utf-8">
<title>Tagmorrow – ID Systems, Supplies, Services and Accessories</title>
<link href="https://fonts.googleapis.com/css2?family=Arimo:wght@400;700&family=PT+Serif:ital@1&display=swap" rel="stylesheet">
<style>
:root{
  --blue:#3565b3;
  --blue-bright:#1a8fd6;
  --ink:#222;
  --muted:#8a8a8a;
  --panel:#f2f2f2;
  --tile-head:#ececec;
  --dark:#333;
  --footer:#f4f4f4;
  --footer-bar:#ebebeb;
  --line:#e2e2e2;
}
*{margin:0;padding:0;box-sizing:border-box}
html,body{width:1200px;height:1179px;overflow:hidden;background:#fff}
body{font-family:"Arimo",Arial,sans-serif;color:var(--ink);position:relative}
a{color:inherit;text-decoration:none}
.abs{position:absolute}

.site-header{position:absolute;left:0;top:0;width:1200px;height:114px;background:linear-gradient(#fff,#f3f3f3);border-bottom:1px solid var(--line)}
.account-links{left:957px;top:0;width:123px;height:27px;background:var(--blue-bright);color:#fff;font-size:12px;line-height:27px;text-align:center;border-radius:0 0 3px 3px}
.brand{left:120px;top:44px;display:flex;align-items:center;gap:12px;color:var(--blue);font-size:40px;line-height:1}
.brand-dot{width:22px;height:22px;border-radius:50%;background:var(--blue)}
.tagline{left:390px;top:32px;font-family:"PT Serif",Georgia,serif;font-style:italic;font-size:22px;color:#111}
.main-nav{left:625px;top:84px;display:flex;font-size:12px}
.main-nav a{padding:0 11px;height:29px;line-height:15px;margin-left:2px}
.main-nav a.current{color:var(--blue-bright);border-bottom:2px solid var(--blue-bright)}

.hero{left:120px;top:138px;width:680px;height:270px;background:var(--blue);overflow:hidden}
.hero-photo{position:absolute;left:300px;top:0;width:380px;height:270px;background:linear-gradient(90deg,var(--blue) 0%,#8fa6cf 35%,#e4e8ee 70%,#f3f4f6 100%)}
.hero-title{position:absolute;left:24px;top:66px;color:#fff;font-size:24px;line-height:32px}
.hero-title span{display:block;padding-left:72px}
.hero-text{position:absolute;left:26px;top:154px;width:275px;color:#fff;font-size:14px;line-height:17px;text-align:justify}

.section-title{left:120px;top:442px;font-size:20px;color:var(--blue)}
.tile{position:absolute;width:165px;height:183px;border:1px solid var(--line);background:#fff}
.tile-head{height:45px;background:var(--tile-head);display:flex;align-items:center;justify-content:center;text-align:center;font-size:14px;line-height:17px}
.tile-photo{height:136px}

.side-box{position:absolute;left:850px;width:230px}
.side-head{height:43px;background:var(--blue);color:#fff;font-size:20px;line-height:43px;padding-left:14px}
.news-body{background:var(--panel);height:227px;padding:14px 12px 0;font-size:12px;color:var(--muted);line-height:14.5px}
.news-item{margin-bottom:23px}
.news-item b{font-weight:700;color:#888;letter-spacing:.3px}
.read-more{position:absolute;right:12px;bottom:7px;color:var(--blue);font-size:12px}
.newsletter{top:426px;height:177px;background:var(--dark);color:#fff;padding:11px 12px}
.newsletter h3{font-weight:400;font-size:20px;margin-bottom:9px}
.newsletter p{font-size:12px;line-height:16px;letter-spacing:.2px}
.email-field{margin-top:13px;height:30px;background:#fff;border-radius:3px;color:#333;font-size:13px;line-height:30px;padding-left:10px}
.signup{position:absolute;right:19px;top:132px;width:72px;height:29px;background:var(--blue-bright);border-radius:3px;font-size:14px;line-height:29px;text-align:center}
.featured-body{background:var(--panel);height:204px;padding:8px 12px 0 14px;font-size:12px;line-height:14px}
.featured-photo{width:204px;height:140px;border:2px solid #ddd;background:radial-gradient(#9a9a9a,#d8d8d8 55%,#fff 80%);margin-bottom:12px}

.site-footer{position:absolute;left:0;top:918px;width:1200px;height:214px;background:var(--footer)}
.foot-col{position:absolute;top:20px;font-size:12px;color:var(--muted);letter-spacing:.3px}
.foot-col h4{font-weight:400;font-size:14px;color:#555;margin-bottom:19px;margin-left:-2px}
.foot-col li{list-style:none;height:24px}
.contact-row{display:flex;gap:10px;margin-bottom:20px;line-height:14px}
.contact-row svg{flex:none;margin-top:1px}
.foot-brand{left:866px;top:1035px;display:flex;align-items:center;gap:10px;color:#9a9a9a;font-size:34px}
.foot-brand i{width:18px;height:18px;border-radius:50%;background:#9a9a9a}
.footer-bar{position:absolute;left:0;top:1132px;width:1200px;height:47px;background:var(--footer-bar);border-top:1px solid #d6d6d6}
.copyright{position:absolute;left:116px;top:16px;font-size:12px;color:var(--muted);letter-spacing:.5px}
.social{position:absolute;top:10px;width:24px;height:24px;background:#9a9a9a;border-radius:2px}
</style>
</head>
<body>

<header class="site-header">
  <a class="abs account-links" href="#">Order Now &nbsp;|&nbsp; Login</a>
  <div class="abs brand"><span class="brand-dot"></span>tagmorrow</div>
  <p class="abs tagline">ID Systems, Supplies, Services and Accessories</p>
  <nav class="abs main-nav">
    <a class="current" href="#">Home</a><a href="#">About Us</a><a href="#">Our Products</a><a href="#">Our Services</a><a href="#">News</a><a href="#">Contact Us</a>
  </nav>
</header>

<section class="abs hero">
  <div class="hero-photo" role="img" aria-label="Card printer with printed ID cards"></div>
  <h1 class="hero-title" style="font-weight:400">Lorem ipsum dolor sit amet <span>consectetur adipiscing elit</span></h1>
  <p class="hero-text">Lorem ipsum dolor sit amet, consectetur adipiscing elit. Morbi luctus sagittis sapien, nec pharetra neque porttitor in.</p>
</section>

<h2 class="abs section-title" style="font-weight:400">Everything you will ever need in ID Supplies….</h2>

<div class="tile" style="left:120px;top:476px"><div class="tile-head">Card Printers<br>And Ribbons</div><div class="tile-photo" role="img" aria-label="Card printer and ribbon" style="background:linear-gradient(135deg,#dde7f0,#3aa3c9 50%,#f2f2f2)"></div></div>
<div class="tile" style="left:292px;top:476px"><div class="tile-head">Solutions</div><div class="tile-photo" role="img" aria-label="Printed ID cards" style="background:linear-gradient(135deg,#fff,#3f6fb8 50%,#f4f4f4)"></div></div>
<div class="tile" style="left:463px;top:476px"><div class="tile-head">Bureau Services</div><div class="tile-photo" role="img" aria-label="Fanned stack of coloured cards" style="background:linear-gradient(160deg,#fff 20%,#4d86c8 50%,#e8b43a 65%,#fff 85%)"></div></div>
<div class="tile" style="left:635px;top:476px"><div class="tile-head">Laminates</div><div class="tile-photo" role="img" aria-label="Laminated ID card" style="background:linear-gradient(135deg,#f4f4f4,#d8c9cf 50%,#eee)"></div></div>

<div class="tile" style="left:120px;top:684px"><div class="tile-head">Lanyards</div><div class="tile-photo" role="img" aria-label="Colourful printed lanyards" style="background:linear-gradient(135deg,#fff,#e8c13a 35%,#d6367a 55%,#fff)"></div></div>
<div class="tile" style="left:292px;top:684px"><div class="tile-head">Wristbands</div><div class="tile-photo" role="img" aria-label="Coloured silicone wristbands" style="background:radial-gradient(#fff 20%,#e0542e 45%,#3a7ac8 60%,#fff 75%)"></div></div>
<div class="tile" style="left:463px;top:684px"><div class="tile-head">Card Holders</div><div class="tile-photo" role="img" aria-label="Clear plastic card holder" style="background:linear-gradient(#fff,#e6ecf2 50%,#fff)"></div></div>
<div class="tile" style="left:635px;top:684px"><div class="tile-head">Accessories</div><div class="tile-photo" role="img" aria-label="Badge reels and clips" style="background:linear-gradient(135deg,#ddd,#5ab84a 55%,#2f9e2f)"></div></div>

<aside class="side-box" style="top:138px">
  <div class="side-head">Whats New</div>
  <div class="news-body">
    <p class="news-item"><b>Lorem ipsum dolor sit amet,</b><br>Consectetur adipiscing elit. Vivamus<br>&nbsp;quis turpis dapibus.</p>
    <p class="news-item"><b>Lorem ipsum dolor sit amet,</b><br>Consectetur adipiscing elit. Vivamus<br>&nbsp;quis turpis dapibus.</p>
    <p class="news-item"><b>Lorem ipsum dolor sit amet,</b><br>Consectetur adipiscing elit. Vivamus<br>&nbsp;quis turpis dapibus.</p>
    <a class="read-more" href="#">Read More &gt;</a>
  </div>
</aside>

<aside class="side-box newsletter">
  <h3>Newsletter Signup</h3>
  <p>Enter your email address below to recieve our monthly newsletter.</p>
  <div class="email-field">Email address</div>
  <a class="signup" href="#">Signup</a>
</aside>

<aside class="side-box" style="top:620px">
  <div class="side-head">Featured Products</div>
  <div class="featured-body">
    <div class="featured-photo" role="img" aria-label="Grey desktop card printer"></div>
    <p>Lorem ipsum dolor sit amet, consecte adipiscing elit.</p>
  </div>
</aside>

<footer class="site-footer">
  <div class="foot-col" style="left:118px"><h4>Navigation</h4><ul><li>Home</li><li>About Us</li><li>Our Products</li><li>Our Services</li><li>News</li><li>Contact Us</li></ul></div>
  <div class="foot-col" style="left:293px"><h4>Our Services</h4><ul><li>Suspendisse</li><li>Nullam fermentum</li><li>Integer ornare</li><li>Proin iaculis</li><li>Praesent ac</li></ul></div>
  <div class="foot-col" style="left:471px"><h4>Our Products</h4><ul><li>Suspendisse</li><li>Nullam fermentum</li><li>Integer ornare</li><li>Proin iaculis</li><li>Praesent ac</li></ul></div>
  <div class="foot-col" style="left:654px"><h4>Contact us</h4>
    <div class="contact-row"><svg width="11" height="12" viewBox="0 0 11 12"><path d="M5.5 0a4 4 0 0 0-4 4c0 3 4 8 4 8s4-5 4-8a4 4 0 0 0-4-4zm0 5.5a1.5 1.5 0 1 1 0-3 1.5 1.5 0 0 1 0 3z" fill="#aaa"/></svg><span>18/32 Calder Street, Glen Ashby,<br>Victoria, 3152 Australia</span></div>
    <div class="contact-row"><svg width="11" height="12" viewBox="0 0 11 12"><path d="M2 0l2 3-1 1.5c.7 1.6 2 2.9 3.5 3.5L8 7l3 2-1 2.5C5 11 .5 6.5 0 1.5z" fill="#aaa"/></svg><span>(03)9000 1234</span></div>
    <div class="contact-row"><svg width="11" height="12" viewBox="0 0 11 12"><rect x="0" y="3" width="11" height="7" fill="#aaa"/><path d="M0 3l5.5 4L11 3" stroke="#f4f4f4" fill="none"/></svg><span>info@tagmorrow.com.au</span></div>
  </div>
</footer>
<div class="abs foot-brand"><i></i>tagmorrow</div>

<div class="footer-bar">
  <p class="copyright">Copyright © 2013 tagmorrow. All Right Reserved.</p>
  <span class="social" style="left:976px" aria-label="Social link"></span>
  <span class="social" style="left:1015px" aria-label="Social link"></span>
  <span class="social" style="left:1053px" aria-label="Social link"></span>
</div>

</body>
</html>
```